" Empresa de desenvolvimento humano, que trabalha principalmente a gestão dentro do ambiente de trabalho através de treinamento, consultoria e coaching. O principal conceito é que cada pessoa é única e seu auto-conhecimento é a chave para seu sucesso. "

```html
<!DOCTYPE html>
<html lang="pt-BR">
<head>
<meta charset="UTF-8">
<title>Título da Página</title>
<link rel="stylesheet" href="https://fonts.googleapis.com/css2?family=Roboto:wght@400;500;700&display=swap">
<style>
  :root {
    --backdrop: #dcdcdc;
    --paper: #ffffff;
    --brand-blue: #1f9ad8;
    --brand-blue-light: #8fd0f2;
    --ink: #2b2b2b;
    --logo-ink: #33414f;
  }
  html, body {
    margin: 0;
    padding: 0;
    width: 1200px;
    height: 1200px;
    overflow: hidden;
    background: var(--backdrop);
  }
  .canvas {
    position: relative;
    width: 1200px;
    height: 1200px;
    background: var(--backdrop);
    font-family: "Roboto", Arial, sans-serif;
  }
  .page {
    position: absolute;
    left: 0;
    top: 257px;
    width: 1200px;
    height: 679px;
    background: var(--paper);
    overflow: hidden;
  }
  .page-art {
    position: absolute;
    inset: 0;
    width: 1200px;
    height: 679px;
  }
  .page-title {
    position: absolute;
    left: 505px;
    top: 62px;
    margin: 0;
    font-weight: 500;
    font-size: 36px;
    line-height: 39px;
    color: var(--brand-blue);
    letter-spacing: 0.5px;
  }
  .page-body {
    position: absolute;
    left: 792px;
    top: 44px;
    width: 350px;
    height: 440px;
    margin: 0;
    overflow: hidden;
    font-size: 16.6px;
    line-height: 26.3px;
    color: var(--ink);
    text-align: justify;
  }
  .brand {
    position: absolute;
    left: 912px;
    top: 562px;
    display: flex;
    align-items: center;
    gap: 14px;
  }
  .brand-mark {
    width: 22px;
    height: 22px;
    background: var(--brand-blue);
  }
  .brand-name {
    font-weight: 500;
    font-size: 34px;
    letter-spacing: 2px;
    color: var(--logo-ink);
  }
</style>
</head>
<body>
<div class="canvas">
  <section class="page">
    <svg class="page-art" viewBox="0 0 1200 679" xmlns="http://www.w3.org/2000/svg">
      <defs>
        <linearGradient id="photoTone" x1="0" y1="0" x2="1" y2="1">
          <stop offset="0" stop-color="#4a5563"/>
          <stop offset="0.45" stop-color="#7a6552"/>
          <stop offset="1" stop-color="#2f6f8f"/>
        </linearGradient>
        <clipPath id="photoArea">
          <polygon points="0,0 360,0 900,679 0,679"/>
        </clipPath>
      </defs>
      <polygon role="img" aria-label="Foto de um aperto de mãos sobre uma mesa de escritório com documentos e notebook"
               points="0,0 360,0 900,679 0,679" fill="url(#photoTone)"/>
      <g clip-path="url(#photoArea)">
        <polygon class="stripe-dark" points="235,0 292,0 410,155 352,155" fill="var(--brand-blue)"/>
        <polygon class="stripe-light" points="305,0 372,0 446,92 395,92" fill="var(--brand-blue-light)"/>
      </g>
    </svg>

    <h1 class="page-title">TÍTULO DA<br>PÁGINA</h1>

    <p class="page-body">Ao contrário do que se acredita, Lorem Ipsum não é simplesmente um texto randômico. Com mais de 2000 anos, suas raízes podem ser encontradas em uma obra de literatura latina clássica datada de 45 AC. Ricardo Almeida, um professor de latim do Colégio Monte Sereno na Virgínia, pesquisou uma das mais obscuras palavras em latim, consectetur, oriunda de uma passagem de Lorem Ipsum, e, procurando por entre citações da palavra na literatura clássica, descobriu a sua indubitável origem. Lorem Ipsum vem das seções 1.10.32 e 1.10.33 do "de Finibus Bonorum et Malorum" (Os Extremos do Bem e do Mal), de Túlio Máximo, escrito em 45 AC. Este livro é um tratado de teoria da ética muito popular na época da</p>

    <div class="brand">
      <span class="brand-mark"></span>
      <span class="brand-name">ESSENTIA</span>
    </div>
  </section>
</div>
</body>
</html>
```